Business Card Re-Design/Update

We'd like to update out business cards. I've included our current "Style guide" which has the colour scheme of the organisation in it. I've also included the branding files with logos etc in them.

I've also included a copy of one of our existing cards so that you can see how ugly/dated they look. I'd like a fresh modern corporate look.

Target Market(s)

These are for our clients, potential clients, industry contacts - like all business cards

Contact Information for Business Card

Name
Position
Company Address - Level 1, 47 Garnet Lane, Toowong Qld 4066
Direct Phone
mobile
Email
Website -www.korvalnet.com.au
Logo

Colors

Designer to choose colors to be used in the design.

Requirements
Must have
• Main Logo
• Cards will need to be editable to be able to personalize them for each new employee.
Nice to have
• The MapOUT, HandOVER, UpKEEP would be okay to have if they can be sensibly and professionally added to the look without detracting from the main imagery.
• Maybe they could go on the back of the card? will leave this to your creative discretion as to whether/where they fit.
Should not have
• Should not have decorative or script fonts

```html
<!DOCTYPE html>
<html lang="en">
<head>
<meta charset="utf-8">
<title>korvalnet business card</title>
<link rel="stylesheet" href="https://fonts.googleapis.com/css2?family=Open+Sans:wght@400;600;700&display=swap">
<style>
  :root {
    --backdrop: #1c1c1c;
    --brand-red: #d71f27;
    --ink: #3a3a3c;
    --paper: #ffffff;
    --muted: #555555;
    --map-green: #5aa02c;
    --hand-blue: #2a8fd6;
    --keep-magenta: #b62ea0;
  }
  * { box-sizing: border-box; margin: 0; padding: 0; }
  html, body { width: 1200px; height: 1200px; overflow: hidden; }
  body {
    background: var(--backdrop);
    font-family: "Open Sans", Arial, sans-serif;
    position: relative;
  }
  .card {
    position: absolute;
    left: 320px;
    width: 560px;
    height: 320px;
    background: var(--paper);
    overflow: hidden;
    box-shadow: 0 14px 30px rgba(0,0,0,.55);
  }
  .card--front { top: 210px; }
  .card--back { top: 620px; }

  /* front */
  .front__band {
    position: absolute; left: 0; top: 0; width: 100%; height: 228px;
    background: var(--brand-red);
    display: flex; align-items: center; justify-content: center; gap: 16px;
  }
  .logo-mark { width: 44px; height: 44px; border: 7px solid currentColor; }
  .logo-word { font-weight: 600; letter-spacing: -1px; }
  .front__band .logo { color: var(--paper); display: flex; align-items: center; gap: 16px; }
  .front__band .logo-word { font-size: 60px; }
  .service-row {
    position: absolute; left: 0; bottom: 0; width: 100%; height: 92px;
    display: flex; align-items: center; justify-content: space-around; padding: 0 18px;
  }
  .service { display: flex; align-items: center; gap: 8px; font-size: 24px; font-weight: 600; }
  .service__mark { width: 16px; height: 16px; border: 3px solid currentColor; }
  .service--map { color: var(--map-green); }
  .service--hand { color: var(--hand-blue); }
  .service--keep { color: var(--keep-magenta); }

  /* back */
  .back__logo {
    position: absolute; left: 0; top: 0; width: 270px; height: 100%;
    display: flex; flex-direction: column; align-items: center; justify-content: center; gap: 12px;
    color: var(--brand-red);
  }
  .back__logo .logo-word { font-size: 44px; }
  .back__divider {
    position: absolute; left: 278px; top: 40px; width: 1.5px; height: 240px; background: var(--brand-red);
  }
  .contact { position: absolute; left: 302px; top: 34px; width: 240px; }
  .contact__name { color: var(--brand-red); font-size: 26px; font-weight: 700; line-height: 1.1; }
  .contact__role {
    color: var(--muted); font-size: 11.5px; padding-bottom: 6px;
    border-bottom: 1.5px solid var(--brand-red);
  }
  .contact__address { color: var(--brand-red); font-size: 13px; line-height: 1.35; margin: 14px 0 14px; }
  .contact__list { list-style: none; color: var(--ink); font-size: 11.5px; line-height: 1.45; }
  .contact__list li { display: flex; align-items: center; gap: 6px; }
  .contact__list svg { width: 11px; height: 11px; flex: none; }
  .icon-gap { display: inline-block; width: 11px; flex: none; }
</style>
</head>
<body>
  <section class="card card--front" aria-label="Card front">
    <div class="front__band">
      <div class="logo">
        <span class="logo-mark"></span>
        <span class="logo-word">korvalnet</span>
      </div>
    </div>
    <div class="service-row">
      <span class="service service--map"><span class="service__mark"></span>MapOUT</span>
      <span class="service service--hand"><span class="service__mark"></span>HandOVER</span>
      <span class="service service--keep"><span class="service__mark"></span>UpKEEP</span>
    </div>
  </section>

  <section class="card card--back" aria-label="Card back">
    <div class="back__logo">
      <span class="logo-mark"></span>
      <span class="logo-word">korvalnet</span>
    </div>
    <div class="back__divider"></div>
    <div class="contact">
      <p class="contact__name">Maren Holt</p>
      <p class="contact__role">Business Development Manager</p>
      <p class="contact__address">22/9 Ferris Road,<br>Kelvin Grove QLD 4059</p>
      <ul class="contact__list">
        <li><svg viewBox="0 0 12 12"><rect x="3" y="0.5" width="6" height="11" rx="1" fill="none" stroke="#d71f27" stroke-width="1.2"/><circle cx="6" cy="9.5" r=".7" fill="#d71f27"/></svg>+61 (0)412 555 019</li>
        <li><span class="icon-gap"></span>+61 (0)7 3555 0142</li>
        <li><svg viewBox="0 0 12 12"><path d="M2.5 1.5 L4.5 1.5 L5.2 4 L4 5 Q5 7.2 7 8 L8 6.8 L10.5 7.5 L10.5 9.5 Q6 10.5 2.5 5 Z" fill="#d71f27"/></svg>+61 (0)7 3555 0100</li>
        <li><span class="icon-gap"></span>+61 (0)7 3555 0199</li>
        <li><span class="icon-gap"></span>mholt@korvalnet.com.au</li>
        <li><svg viewBox="0 0 12 12"><circle cx="6" cy="6" r="5" fill="none" stroke="#d71f27" stroke-width="1"/><ellipse cx="6" cy="6" rx="2.2" ry="5" fill="none" stroke="#d71f27" stroke-width=".9"/><line x1="1" y1="6" x2="11" y2="6" stroke="#d71f27" stroke-width=".9"/></svg>www.korvalnet.com.au</li>
      </ul>
    </div>
  </section>
</body>
</html>
```